Minimalist Modern Business Card Design, open to ideas, or cleaner version of provided files, but what logo & logo colors (with some black) as shown in files, and info for back shown in files as well.

```html
<!DOCTYPE html>
<html lang="en">
<head>
<meta charset="utf-8">
<title>Harbor Route Works – Business Card</title>
<link rel="stylesheet" href="https://fonts.googleapis.com/css2?family=Montserrat:wght@400;500;600;700&display=swap">
<style>
  :root {
    --backdrop: #aaaaaa;
    --card-light: #ffffff;
    --card-dark: #232323;
    --brand-grey: #b3b3b3;
    --ink: #222222;
    --ink-soft: #6e6e6e;
    --white: #ffffff;
  }
  * { box-sizing: border-box; margin: 0; padding: 0; }
  html, body {
    width: 1200px;
    height: 1000px;
    overflow: hidden;
    background: var(--backdrop);
    font-family: "Montserrat", sans-serif;
  }
  .canvas { position: relative; width: 1200px; height: 1000px; }
  .card {
    position: absolute;
    left: 294px;
    width: 613px;
    height: 351px;
    border-radius: 22px;
    box-shadow: 0 18px 40px rgba(0,0,0,0.28);
    overflow: hidden;
  }
  .card--front { top: 96px; background: var(--card-light); }
  .card--back { top: 518px; background: var(--card-dark); }

  .brand {
    position: absolute;
    left: 43px;
    top: 66px;
    display: flex;
    align-items: center;
    gap: 30px;
    color: var(--brand-grey);
  }
  .brand__square { width: 70px; height: 70px; background: var(--brand-grey); }
  .brand__name {
    font-weight: 600;
    font-size: 37px;
    line-height: 36px;
  }

  .contact {
    position: absolute;
    right: 64px;
    top: 220px;
    text-align: right;
    color: var(--ink);
  }
  .contact__name { font-weight: 700; font-size: 17px; letter-spacing: 0.3px; }
  .contact__role {
    margin-top: 4px;
    font-size: 9px;
    letter-spacing: 4.2px;
    margin-right: -4px;
    color: var(--ink-soft);
  }
  .contact__lines { margin-top: 18px; font-size: 14px; line-height: 17px; color: var(--ink-soft); }
  .contact__label { font-weight: 700; color: #555; }

  .back-pattern { position: absolute; inset: 0; background: var(--card-dark); }
  .back-brand {
    position: absolute;
    left: 416px;
    top: 240px;
    color: var(--white);
    font-weight: 600;
    font-size: 13px;
    line-height: 14px;
  }
</style>
</head>
<body>
<main class="canvas">
  <section class="card card--front">
    <div class="brand">
      <span class="brand__square"></span>
      <span class="brand__name">Harbor<br>Route Works</span>
    </div>
    <div class="contact">
      <p class="contact__name">NAME SURNAME</p>
      <p class="contact__role">PRESIDENT</p>
      <p class="contact__lines">
        <span class="contact__label">m:</span> 123-456-7890<br>
        <span class="contact__label">e:</span> email@website.com
      </p>
    </div>
  </section>

  <section class="card card--back">
    <div class="back-pattern" role="img" aria-label="Faint repeating brand pattern on dark background"></div>
    <p class="back-brand">Harbor<br>Route Works</p>
  </section>
</main>
</body>
</html>
```